Electrical construction, completion and commissioning
Keystone Ridge Services
Use same font as used in my logo
not sure may try a few options
Professional
Callum Brody
Director
PO Box 7819 East Perth WA 6892
callum@keystoneridgeservices.com.au
keystoneridgeservices.com.au
EC 20735
ABN 48 271 502 936
Electrical Construction Engineering Completions Commissioning Management and Supervision

```html
<!DOCTYPE html>
<html lang="en">
<head>
<meta charset="utf-8">
<title>Keystone Ridge Services – Business Card</title>
<link href="https://fonts.googleapis.com/css2?family=Michroma&display=swap" rel="stylesheet">
<style>
  :root {
    --page-bg: #d9dadc;
    --card-white: #ffffff;
    --card-blue-light: #7fb3e3;
    --card-blue-dark: #3f84c8;
    --brand-blue: #2f79c2;
    --brand-green: #7bb13c;
    --text-grey: #5c6670;
    --white: #ffffff;
  }
  * { box-sizing: border-box; margin: 0; padding: 0; }
  html, body {
    width: 1200px; height: 919px; overflow: hidden;
    background: var(--page-bg);
    font-family: "Michroma", sans-serif;
  }
  .canvas { position: relative; width: 1200px; height: 919px; }
  .card {
    position: absolute;
    width: 520px; height: 297px;
    box-shadow: 0 6px 18px rgba(0,0,0,0.18);
  }

  /* Front */
  .card-front { left: 50px; top: 480px; background: var(--card-white); }
  .front-brand {
    position: absolute; top: 88px; left: 0; right: 0;
    display: flex; align-items: center; justify-content: center; gap: 12px;
  }
  .brand-dot {
    width: 22px; height: 22px; border-radius: 50%;
    background: var(--brand-blue); flex: none;
  }
  .brand-name {
    font-size: 19px; color: var(--brand-blue);
    letter-spacing: 1px; font-variant: small-caps; white-space: nowrap;
  }
  .person {
    position: absolute; top: 170px; left: 0; right: 0;
    text-align: center; font-size: 9px; color: var(--text-grey);
    font-variant: small-caps; letter-spacing: 1px;
  }
  .person .name { color: var(--brand-blue); }
  .person .sep { margin: 0 8px; }
  .contacts {
    position: absolute; left: 22px; right: 22px; bottom: 34px;
    font-size: 7px; color: var(--text-grey);
    font-variant: small-caps; letter-spacing: 0.4px;
    display: flex; flex-wrap: wrap; justify-content: center; gap: 6px 14px;
  }
  .contact { display: flex; align-items: center; gap: 4px; white-space: nowrap; }
  .contact svg { width: 9px; height: 9px; flex: none; }

  /* Back */
  .card-back {
    left: 630px; top: 140px;
    background: linear-gradient(135deg, var(--card-blue-light), var(--card-blue-dark));
  }
  .back-brand {
    position: absolute; left: 30px; top: 30px;
    display: flex; align-items: center; gap: 10px;
  }
  .back-brand .brand-dot { background: var(--white); width: 18px; height: 18px; }
  .back-brand .brand-name { color: var(--white); font-size: 12px; }
  .services {
    position: absolute; right: 26px; top: 92px;
    list-style: none; text-align: right;
    color: var(--white); font-size: 11px;
    font-variant: small-caps; letter-spacing: 1.2px;
  }
  .services li {
    margin-bottom: 20px; white-space: nowrap;
    display: flex; align-items: center; justify-content: flex-end; gap: 10px;
  }
  .services li:last-child { margin-bottom: 0; }
  .services li::after {
    content: ""; width: 5px; height: 5px; border-radius: 50%;
    background: var(--white); flex: none;
  }
</style>
</head>
<body>
<main class="canvas">

  <section class="card card-front" aria-label="Business card front">
    <div class="front-brand">
      <span class="brand-dot"></span>
      <span class="brand-name">Keystone Ridge Services</span>
    </div>
    <p class="person">
      <span class="name">Callum Brody</span><span class="sep">|</span><span class="role">Director</span>
    </p>
    <div class="contacts">
      <span class="contact">
        <svg viewBox="0 0 10 10"><circle cx="5" cy="5" r="5" fill="#2f79c2"/><rect x="2.5" y="3.3" width="5" height="3.4" fill="#fff"/></svg>
        callum@keystoneridgeservices.com.au
      </span>
      <span class="contact">
        <svg viewBox="0 0 10 10"><circle cx="5" cy="5" r="5" fill="#2f79c2"/><circle cx="5" cy="4.3" r="1.6" fill="#fff"/></svg>
        PO Box 7819 Harlow Bay NR 7104
      </span>
      <span class="contact">
        <svg viewBox="0 0 10 10"><circle cx="5" cy="5" r="5" fill="#7bb13c"/><rect x="3.8" y="2.4" width="2.4" height="5.2" rx="0.6" fill="#fff"/></svg>
        0438 217 905
      </span>
      <span class="contact">
        <svg viewBox="0 0 10 10"><circle cx="5" cy="5" r="5" fill="#2f79c2"/><circle cx="5" cy="5" r="2.6" fill="none" stroke="#fff" stroke-width="0.9"/></svg>
        keystoneridgeservices.com.au
      </span>
    </div>
  </section>

  <section class="card card-back" aria-label="Business card back">
    <div class="back-brand">
      <span class="brand-dot"></span>
      <span class="brand-name">Keystone Ridge Services</span>
    </div>
    <ul class="services">
      <li>Electrical Construction</li>
      <li>Engineering</li>
      <li>Completions</li>
      <li>Commissioning</li>
      <li>Management and supervision</li>
    </ul>
  </section>

</main>
</body>
</html>
```